Business Consulting Business Card

professional business card with basic information (1) First and Last name (2) email address, (3) phone number, (4) website.

```html
<!DOCTYPE html>
<html lang="en">
<head>
<meta charset="utf-8">
<title>Bay Meridian Business Card</title>
<link rel="stylesheet" href="https://fonts.googleapis.com/css2?family=Montserrat:wght@500&family=Poppins:wght@400;500&display=swap">
<style>
  :root {
    --backdrop: #d9d9db;
    --paper: #ffffff;
    --navy-light: #0b2238;
    --navy-dark: #010a16;
    --teal: #2fa9c2;
    --teal-mark: #3bb3b6;
    --ink: #2b2f36;
    --rule: #8a8f96;
    --edge: #2aa3bd;
  }
  * { box-sizing: border-box; margin: 0; padding: 0; }
  html, body { width: 1200px; height: 800px; overflow: hidden; }
  body {
    background: var(--backdrop);
    font-family: "Poppins", sans-serif;
    position: relative;
  }
  .card {
    position: absolute;
    width: 560px;
    height: 320px;
    left: 320px;
    border-bottom: 3px solid var(--edge);
    box-shadow: 0 8px 22px rgba(0,0,0,0.18);
  }
  .card-front { top: 50px; background: var(--paper); }
  .card-back {
    top: 430px;
    background: radial-gradient(ellipse at 35% 40%, var(--navy-light), var(--navy-dark) 75%);
    display: flex;
    align-items: center;
    justify-content: center;
    gap: 22px;
  }

  /* front */
  .brand-block {
    position: absolute;
    left: 40px;
    top: 110px;
    width: 180px;
    display: flex;
    flex-direction: column;
    align-items: center;
    gap: 10px;
  }
  .brand-dot {
    width: 54px; height: 54px; border-radius: 50%;
    background: var(--teal-mark);
  }
  .brand-name {
    font-family: "Montserrat", sans-serif;
    font-weight: 500;
    font-size: 14px;
    letter-spacing: 3px;
    color: var(--teal-mark);
  }
  .divider {
    position: absolute;
    left: 245px; top: 78px;
    width: 1px; height: 120px;
    background: var(--rule);
  }
  .contact {
    position: absolute;
    left: 268px; top: 66px;
  }
  .person-name {
    font-size: 21px;
    font-weight: 400;
    color: var(--teal);
    letter-spacing: 0.5px;
    line-height: 1.1;
  }
  .person-title {
    font-size: 12px;
    font-weight: 500;
    color: var(--ink);
    margin-bottom: 6px;
  }
  .contact-list { list-style: none; }
  .contact-list li {
    display: flex; align-items: center; gap: 8px;
    font-size: 12px; color: var(--ink);
    line-height: 17px;
  }
  .contact-list svg { width: 10px; height: 10px; fill: var(--teal); flex: none; }
  .address {
    position: absolute;
    left: 0; right: 0; bottom: 28px;
    text-align: center;
    font-size: 12px;
    color: var(--ink);
  }

  /* back */
  .back-dot {
    width: 58px; height: 58px; border-radius: 50%;
    background: var(--teal-mark);
  }
  .back-name {
    font-family: "Montserrat", sans-serif;
    font-weight: 500;
    font-size: 32px;
    letter-spacing: 7px;
    color: #ffffff;
  }
</style>
</head>
<body>
  <section class="card card-front">
    <div class="brand-block">
      <div class="brand-dot"></div>
      <div class="brand-name">BAY MERIDIAN</div>
    </div>
    <div class="divider"></div>
    <div class="contact">
      <h1 class="person-name">DANIEL REYES</h1>
      <p class="person-title">President</p>
      <ul class="contact-list">
        <li><svg viewBox="0 0 10 10"><path d="M2 0.5 L4 2.5 L3 3.8 Q4.2 6 6.2 7 L7.5 6 L9.5 8 L8 9.6 Q3 9 0.4 2 Z"/></svg>412-308-7741</li>
        <li><svg viewBox="0 0 10 10"><path d="M2.5 0 H7.5 V10 H2.5 Z M3.5 1 V8 H6.5 V1 Z"/></svg>412-308-7742</li>
        <li><svg viewBox="0 0 10 10"><path d="M2.5 0 H7 V3 H9.5 V9.5 H0.5 V3 H2.5 Z M3.5 1 V3 H6 V1 Z M2 5 H8 V6 H2 Z"/></svg>412-308-7743</li>
        <li><svg viewBox="0 0 10 10"><path d="M0.5 2 H9.5 V8.5 H0.5 Z M1.3 2.6 L5 5.6 L8.7 2.6 Z"/></svg>hello@baymeridian.com</li>
        <li><svg viewBox="0 0 10 10"><circle cx="5" cy="5" r="4.6"/></svg>www.baymeridian.com</li>
      </ul>
    </div>
    <p class="address">214 Harbor View Road, Juneau, Alaska 99801</p>
  </section>

  <section class="card card-back">
    <div class="back-dot"></div>
    <div class="back-name">BAY MERIDIAN</div>
  </section>
</body>
</html>
```